Save Us! Grand Opening Rescue + Outreach Center Flyers for our Animals

Flyers to describe the different areas and animals in our new rescue + outreach center. We are a charity that rescues animals from animal testing and other forms of abuse. We have a grand opening next month and need great descriptive flyers in order to educate people and raise funds.
Updates

I need to provide more information for the designers.

Target Market(s)

Those interested in donating, volunteering and helping us save animals.

Industry/Entity Type

Non-Profit

Font styles to use
Sans Serif

Colors

Designer to choose colors to be used in the design.

Requirements
Must have
• Colors and photos. Feel free to edit the Dusty photos to make them fit in the flyer, use 1 or both, whatever you like.
• Here is the text for the main flyer, although there are a few flyers, but they can be interchangeable:
• Senior & Special Needs Dogs
• At the TEL, these dogs will have their very own retreat and retirement center to experience the best in care & relaxation!
• Survivor Spotlight: Dusty
• Dusty was rescued by KHW after being abandoned. His lower body was completely paralyzed, unable to use his hind legs. After nearly 1 year of rehabilitation, KHW found him his forever family and Dusty is in a specialized wheelchair so he can run and play with his forever family, and be the puppy he is!
• Help us enrich the lives of our senior & special needs dogs by donating today and save more survivors, just like Dusty!
• Questions about donating to the TEL? Please contact our President at gretchen@khwrescue.org
Nice to have
• Playful.
Should not have
• No sharp edges, not too serious, yet has a point - asking for donations and educational aspect must come across.

```html
<!DOCTYPE html>
<html lang="en">
<head>
<meta charset="utf-8">
<title>Senior &amp; Special Needs Dogs – TEL</title>
<link href="https://fonts.googleapis.com/css2?family=Rammetto+One&family=Open+Sans:wght@700&display=swap" rel="stylesheet">
<style>
  :root {
    --red-orange: #f15a2b;
    --orange: #f7941d;
    --ink: #1a1a1a;
    --white: #ffffff;
    --photo-dark: #2b3a1f;
    --photo-light: #6f9a3c;
  }
  * { margin: 0; padding: 0; box-sizing: border-box; }
  html, body { width: 928px; height: 1200px; overflow: hidden; }
  body { font-family: "Rammetto One", "Arial Black", sans-serif; }
  .flyer {
    position: relative;
    width: 928px;
    height: 1200px;
    background: var(--red-orange);
    overflow: hidden;
  }
  .header-band {
    position: absolute; left: 0; top: 0; width: 100%; height: 147px;
    background: var(--red-orange);
    display: flex; align-items: center; justify-content: center;
  }
  .title {
    color: var(--white);
    font-size: 44px;
    font-weight: 400;
    line-height: 1;
    letter-spacing: 0.5px;
  }
  .orange-field {
    position: absolute; left: 0; top: 147px; width: 100%; height: 670px;
    background: var(--orange);
  }
  .divider {
    position: absolute; left: 0; top: 390px; width: 100%;
    border-top: 2px dashed rgba(255,255,255,0.8);
  }
  .logo {
    position: absolute; left: 66px; top: 136px; width: 236px; height: 236px;
    border-radius: 50%;
    background: var(--white);
    display: flex; align-items: center; justify-content: center;
  }
  .logo-name { font-size: 48px; line-height: 1; color: var(--ink); }
  .intro {
    position: absolute; left: 398px; top: 206px; width: 410px;
    font-size: 18px; line-height: 29.5px; color: var(--ink);
  }
  .intro .accent { color: var(--white); }
  .photo {
    position: absolute; left: 0; top: 0; width: 928px; height: 1200px;
  }
  .name-tag {
    position: absolute; left: 295px; top: 462px; width: 244px; height: 72px;
    background: var(--red-orange);
    color: var(--white);
    font-size: 40px; line-height: 1;
    display: flex; align-items: center; justify-content: center;
  }
  .spotlight-label {
    position: absolute; left: 320px; top: 418px; z-index: 2;
    font-size: 29px; line-height: 36px; font-weight: 400; color: var(--white);
    white-space: nowrap;
  }
  .bio {
    position: absolute; left: 575px; top: 486px; width: 292px;
    font-size: 15.5px; line-height: 22.4px; color: var(--ink);
  }
  .appeal {
    position: absolute; left: 582px; top: 866px; width: 300px;
    font-size: 20px; line-height: 26.5px; color: var(--white);
  }
  .contact-note {
    position: absolute; left: 582px; top: 1050px; width: 270px;
    font-family: "Open Sans", Arial, sans-serif; font-weight: 700;
    font-size: 16.5px; line-height: 21.5px; color: var(--ink);
  }
  .contact-email {
    position: absolute; left: 582px; top: 1130px;
    font-family: "Open Sans", Arial, sans-serif; font-weight: 700;
    font-size: 19px; line-height: 26px; color: var(--white);
  }
</style>
</head>
<body>
<main class="flyer">
  <div class="orange-field"></div>
  <header class="header-band">
    <h1 class="title">Senior &amp; Special Needs Dogs</h1>
  </header>

  <div class="logo"><span class="logo-name">TEL</span></div>
  <p class="intro"><span class="accent">At the TEL</span>, these dogs will have their very own retreat and retirement center to experience the best in care &amp; relaxation!</p>

  <div class="divider"></div>

  <svg class="photo" viewBox="0 0 928 1200" role="img" aria-label="Photo of Dusty, a black puppy in a pink wheelchair wearing an orange bandana, standing on grass">
    <defs>
      <linearGradient id="photoTone" x1="0" y1="0" x2="1" y2="1">
        <stop offset="0" stop-color="#6f9a3c"/>
        <stop offset="0.55" stop-color="#2b3a1f"/>
        <stop offset="1" stop-color="#6f9a3c"/>
      </linearGradient>
    </defs>
    <path d="M0 512 C 190 500, 360 580, 450 730 C 505 830, 520 980, 515 1200 L 0 1200 Z" fill="url(#photoTone)"/>
  </svg>

  <div class="name-tag">Dusty</div>
  <h2 class="spotlight-label">Survivor Spotlight:</h2>
  <p class="bio">Dusty was rescued by KHW after being abandoned. His lower body was completely paralyzed, unable to use his hind legs. After nearly 1 year of rehabilitation, KHW found him his forever family and Dusty is in a specialized wheelchair so he can run and play with his forever family, and be the puppy he is!</p>

  <p class="appeal">Help us enrich the lives of our senior &amp; special needs dogs by donating today and save more survivors, just like Dusty!</p>
  <p class="contact-note">Questions about donating to the TEL? Please contact our President at</p>
  <p class="contact-email">gretchen@khwrescue.org</p>
</main>
</body>
</html>
```